R. T. HOLLOWAY, INC. is a US based Investment firm looking for a five-page website design.

Currently, their temporary site is located at: rtholloway.com and they would like to maintain the site design as much as possible.

R. T. HOLLOWAY, INC. sister companies are: Crestvale Lodge Investments (c-lodge.com) Benwick Petroleum (benwick-petroleum.com) and RTHF (rth-foundation.org/en)

Attached is a .ZIP file with designs and assets we think will be useful for your proposal… Content for the site is attached on: rtholloway website content.docx Current temp website design is attached as: Coming Soon Website.zip .EPS Logo files attached as: rtholloway logos.zip Sample business card attached as: R T Holloway Business cards.eps Other assets, such as Fonts and background images attached as: Assets.zip

Target Market(s)

Investors

Industry/Entity Type

Investments

Number of Pages Required

5+ page

Requirements
Must have
• Contact Page with a form.

```html
<!DOCTYPE html>
<html lang="en">
<head>
<meta charset="utf-8">
<title>R. T. Holloway, Inc.</title>
<link href="https://fonts.googleapis.com/css2?family=Cinzel:wght@400;600;700&family=Open+Sans:wght@400;600&display=swap" rel="stylesheet">
<style>
:root{
  --gold:#b39b5e;
  --gold-soft:#c3ab6f;
  --ink:#272b38;
  --navy:#1f2538;
  --text:#3a3a3a;
  --paper:#f2f1ef;
  --white:#ffffff;
}
*{margin:0;padding:0;box-sizing:border-box}
html,body{width:1200px;height:3805px;overflow:hidden}
body{position:relative;background:var(--white);font-family:"Open Sans",Arial,sans-serif;color:var(--text)}
.abs{position:absolute}
.serif{font-family:"Cinzel",Georgia,serif}

/* header */
.site-header{left:0;top:0;width:1200px;height:786px;background:var(--paper)}
.brand{left:173px;top:20px;width:230px;text-align:center}
.brand-mark{width:58px;height:58px;border:3px solid var(--gold);border-radius:50%;margin:0 auto 8px}
.brand-name{font-family:"Cinzel",Georgia,serif;color:var(--gold);font-size:29px;line-height:32px;letter-spacing:1px}
.brand-inc{font-family:"Cinzel",Georgia,serif;color:var(--gold);font-size:16px;line-height:18px}
.contact-chip{display:flex;align-items:center;gap:8px}
.contact-chip svg{flex:none}
.chip-label{font-size:13px;font-weight:600;color:var(--ink);line-height:16px}
.chip-value{font-size:17px;color:var(--ink);line-height:21px}
.main-nav{left:497px;top:98px;width:530px;display:flex;justify-content:space-between;font-size:12px;font-weight:600;color:var(--ink);letter-spacing:.2px}

.hero-kicker{left:0;top:200px;width:1200px;text-align:center;color:var(--gold);font-size:19px;letter-spacing:1px}
.hero-title{left:0;top:226px;width:1200px;text-align:center;color:var(--ink);font-size:42px;font-weight:700;letter-spacing:1px}
.hero-lead{left:340px;top:301px;width:520px;text-align:center;font-size:13px;line-height:20px;color:var(--ink)}
.hero-art{left:0;top:180px;width:1200px;height:500px;background:linear-gradient(180deg,rgba(242,241,239,0) 0%,rgba(231,106,104,.35) 35%,rgba(36,150,215,.45) 70%,rgba(179,155,94,.5) 100%)}
.hero-band{left:0;top:680px;width:1200px;height:106px;background:var(--ink)}
.dots{left:561px;top:744px;display:flex;gap:12px}
.dots span{width:17px;height:17px;border-radius:50%;background:#7d808a}
.dots span:first-child{background:var(--white)}

/* about */
.about{left:0;top:786px;width:1200px;height:655px;background:#f6f5f2}
.kicker{color:var(--gold);font-family:"Cinzel",Georgia,serif;font-size:18px;letter-spacing:.5px}
.section-title{font-family:"Cinzel",Georgia,serif;font-weight:700;color:var(--ink);font-size:35px;letter-spacing:.5px}
.about-text{left:173px;top:1000px;width:426px;font-size:12px;line-height:28.5px;text-align:justify}
.btn{left:173px;top:1278px;width:118px;height:54px;background:var(--gold);color:var(--white);font-family:"Cinzel",Georgia,serif;font-size:13px;display:flex;align-items:center;justify-content:center}
.about-art{left:665px;top:805px;width:535px;height:525px;background:radial-gradient(circle at 50% 70%,rgba(224,62,72,.35),rgba(246,245,242,0) 60%),linear-gradient(200deg,rgba(23,60,110,.35) 0%,rgba(246,245,242,0) 40%)}

/* mission / vision */
.pillar{top:1595px;width:408px;height:306px;border:3px solid var(--ink);text-align:center;padding:0 20px}
.pillar.vision{border:2px solid var(--gold)}
.pillar-icon{top:1547px;width:98px;height:98px;border-radius:50%;display:flex;align-items:center;justify-content:center}
.pillar .kicker{margin-top:68px;font-size:17px;color:var(--ink)}
.pillar.vision .kicker{color:var(--gold)}
.pillar h2{font-family:"Cinzel",Georgia,serif;font-weight:700;font-size:35px;color:var(--ink);line-height:42px}
.pillar.vision h2{color:var(--gold)}
.pillar p{margin-top:18px;font-size:12px;line-height:25.5px}

/* values */
.values-head{left:0;top:2022px;width:1200px;text-align:center}
.value-card{top:2155px;width:283px;height:263px;background:var(--ink)}
.value-card.gold{background:var(--gold)}
.value-photo{position:absolute;left:5px;top:5px;width:273px;height:195px}
.value-label{position:absolute;left:0;top:200px;width:283px;height:63px;display:flex;align-items:center;justify-content:center;color:var(--white);font-size:19px;letter-spacing:.5px}

/* investment + responsibility */
.invest{left:0;top:2542px;width:600px;height:645px;background:var(--gold)}
.social{left:600px;top:2542px;width:600px;height:645px;background:var(--navy)}
.split-kicker{font-family:"Cinzel",Georgia,serif;font-size:17px}
.split-title{font-family:"Cinzel",Georgia,serif;font-size:30px;letter-spacing:.5px}
.area-icon{width:82px;height:82px;border-radius:50%;background:var(--ink);display:flex;align-items:center;justify-content:center}
.area h3{font-family:"Cinzel",Georgia,serif;font-weight:600;color:var(--ink);font-size:22px;line-height:26px}
.area p{color:var(--white);font-size:13px;line-height:21px;text-align:justify;width:289px}
.social-text{left:630px;top:2822px;width:397px;color:#e8e9ee;font-size:13px;line-height:25.5px;text-align:justify}
.social-text p+p{margin-top:15px}

/* footer */
.site-footer{left:0;top:3187px;width:1200px;height:618px;background:#f7f6f3}
.footer-nav{left:0;top:3629px;width:1200px;text-align:center;font-size:13.5px;font-weight:600;color:var(--ink);letter-spacing:.3px;word-spacing:2px}
.footer-rule{left:173px;top:3689px;width:854px;height:2px;background:var(--ink)}
.copyright{left:0;top:3735px;width:1200px;text-align:center;font-size:13px;font-weight:600;color:var(--ink)}
</style>
</head>
<body>

<!-- header / hero -->
<section class="abs site-header"></section>
<div class="abs hero-art" role="img" aria-label="Illustration of a colourful city skyline with a hand holding a coin and soft clouds"></div>
<div class="abs brand">
  <div class="brand-mark"></div>
  <div class="brand-name">R. T. Holloway</div>
  <div class="brand-inc">Inc.</div>
</div>
<div class="abs contact-chip" style="left:603px;top:26px">
  <svg width="46" height="46" viewBox="0 0 46 46"><circle cx="23" cy="23" r="21" fill="none" stroke="#b39b5e" stroke-width="2"/><rect x="17" y="12" width="12" height="22" rx="2" fill="none" stroke="#b39b5e" stroke-width="2"/><line x1="21" y1="30" x2="25" y2="30" stroke="#b39b5e" stroke-width="2"/></svg>
  <div><div class="chip-label">Phone:</div><div class="chip-value">+1000 000-0000</div></div>
</div>
<div class="abs contact-chip" style="left:798px;top:26px">
  <svg width="46" height="46" viewBox="0 0 46 46"><circle cx="23" cy="23" r="21" fill="none" stroke="#b39b5e" stroke-width="2"/><rect x="13" y="16" width="20" height="14" fill="none" stroke="#b39b5e" stroke-width="2"/><polyline points="13,16 23,24 33,16" fill="none" stroke="#b39b5e" stroke-width="2"/></svg>
  <div><div class="chip-label">Mail:</div><div class="chip-value">info@rtholloway.com</div></div>
</div>
<nav class="abs main-nav"><span>HOME</span><span>ABOUT US</span><span>INVESTMENT AREAS</span><span>SOCIAL RESPONSIBILITY</span><span>CONTACT US</span></nav>

<div class="abs hero-kicker serif">WELCOME TO</div>
<h1 class="abs hero-title serif">R. T. HOLLOWAY, INC</h1>
<p class="abs hero-lead">R. T. Holloway, Inc. helps develop into a great nation and, with assertiveness, stamp its footprint worldwide.</p>
<div class="abs hero-band"></div>
<div class="abs dots"><span></span><span></span><span></span></div>

<!-- about -->
<section class="abs about"></section>
<div class="abs about-art" role="img" aria-label="Illustration of a hand dropping a gold coin into a house with a red roof"></div>
<div class="abs kicker" style="left:173px;top:906px">ABOUT</div>
<h2 class="abs section-title" style="left:173px;top:929px">R. T. HOLLOWAY, INC</h2>
<div class="abs about-text">
  <p>Based in Houston, Texas, R. T. Holloway, Inc. is an investment company, founded in 2010, with the purpose to foster endeavors for socioeconomic development, and create platforms for harnessing the potential of world resources, designed to meet the demands of the emerging markets. R. T. Holloway, Inc. functions as a vehicle that enables investments, with the goal of developing the multiple opportunities available.</p>
  <p>R. T. Holloway, Inc. holds interests in areas of investment that are vital to the international economy: Sectors of Energy, Mining, Industry, Finance and Real Estate.</p>
</div>
<div class="abs btn">READ MORE</div>

<!-- mission / vision -->
<div class="abs pillar" style="left:173px">
  <div class="kicker">OUR</div>
  <h2>MISSION</h2>
  <p>Build a legacy for future generations through a differentiated selection and the development of, safe and high return investment opportunities for our customers, partners, and shareholders, generating a positive impact on the communities it serves.</p>
</div>
<div class="abs pillar-icon" style="left:328px;background:var(--ink)">
  <svg width="56" height="56" viewBox="0 0 56 56" fill="none" stroke="#fff" stroke-width="3"><circle cx="26" cy="30" r="20"/><circle cx="26" cy="30" r="11"/><line x1="26" y1="30" x2="44" y2="12"/><polyline points="38,10 44,12 46,18"/></svg>
</div>
<div class="abs pillar vision" style="left:618px">
  <div class="kicker">OUR</div>
  <h2>VISION</h2>
  <p>R. T. Holloway, Inc. is the main private investment company working towards the diversification and consolidation of national and regional economy.</p>
</div>
<div class="abs pillar-icon" style="left:773px;background:var(--gold)">
  <svg width="60" height="40" viewBox="0 0 60 40" fill="none" stroke="#fff" stroke-width="3"><path d="M4 20 Q30 -4 56 20 Q30 44 4 20Z"/><circle cx="30" cy="20" r="9"/></svg>
</div>

<!-- values -->
<div class="abs values-head">
  <div class="kicker">OUR</div>
  <h2 class="section-title" style="font-size:33px">COMPANY VALUES</h2>
</div>
<div class="abs value-card" style="left:13px"><div class="value-photo" role="img" aria-label="Photo of a man working at a laptop in an office" style="background:linear-gradient(160deg,#dfe4e6,#8a8f93)"></div><div class="value-label">INTEGRITY</div></div>
<div class="abs value-card gold" style="left:310px"><div class="value-photo" role="img" aria-label="Photo of a team meeting around a table with charts" style="background:linear-gradient(160deg,#c9c4bb,#5c5a58)"></div><div class="value-label">EXCELLENCE</div></div>
<div class="abs value-card" style="left:607px"><div class="value-photo" role="img" aria-label="Photo of people reviewing financial charts on a screen" style="background:linear-gradient(160deg,#e2e0de,#6d5e55)"></div><div class="value-label">RESPONSIBILITY</div></div>
<div class="abs value-card gold" style="left:904px"><div class="value-photo" role="img" aria-label="Photo of hands pointing at documents on a desk" style="background:linear-gradient(160deg,#cfc9bf,#7e7467)"></div><div class="value-label">TRANSPARENCY</div></div>

<!-- investment areas -->
<section class="abs invest"></section>
<div class="abs split-kicker" style="left:173px;top:2624px;color:var(--white)">OUR</div>
<h2 class="abs split-title" style="left:173px;top:2647px;color:var(--white)">INVESTMENT AREAS</h2>

<div class="abs area" style="left:173px;top:2733px;display:flex;gap:15px">
  <div class="area-icon"><svg width="44" height="44" viewBox="0 0 44 44" fill="none" stroke="#fff" stroke-width="3"><circle cx="22" cy="22" r="17"/><polygon points="24,10 15,24 22,24 20,34 29,20 22,20" fill="#fff" stroke="none"/></svg></div>
  <div><h3>ENERGY</h3><p>R. T. Holloway, Inc. holds investments both in Exploration &amp; Production, and support field services.</p></div>
</div>
<div class="abs area" style="left:173px;top:2868px;display:flex;gap:15px">
  <div class="area-icon"><svg width="44" height="44" viewBox="0 0 44 44" fill="none" stroke="#fff" stroke-width="3"><path d="M8 14 Q22 2 36 14"/><line x1="22" y1="9" x2="10" y2="34"/><polygon points="26,26 38,26 38,38 22,38" fill="#fff" stroke="none"/></svg></div>
  <div><h3>MINING</h3><p>R. T. Holloway, Inc. holds interests in the management of operations of diamond mines, With current production.</p></div>
</div>
<div class="abs area" style="left:173px;top:3003px;display:flex;gap:15px">
  <div class="area-icon"><svg width="44" height="44" viewBox="0 0 44 44" fill="none" stroke="#fff" stroke-width="3"><polyline points="6,36 6,10 12,10 12,22 20,16 20,22 28,16 28,22 38,16 38,36 6,36"/><rect x="12" y="27" width="4" height="4" fill="#fff"/><rect x="20" y="27" width="4" height="4" fill="#fff"/><rect x="28" y="27" width="4" height="4" fill="#fff"/></svg></div>
  <div><h3>INDUSTRY</h3><p>R. T. Holloway, Inc. holds investments in a paint manufacturing plant with two Warehouses in Viana.</p></div>
</div>

<!-- social responsibility -->
<section class="abs social"></section>
<div class="abs split-kicker" style="left:630px;top:2624px;color:var(--white)">OUR</div>
<h2 class="abs split-title" style="left:630px;top:2647px;color:var(--white)">SOCIAL RESPONSIBILITY</h2>
<div class="abs" role="img" aria-label="Handshake icon" style="left:630px;top:2722px;width:92px;height:70px;background:linear-gradient(135deg,#ffffff,#c9ccd6);border-radius:10px;opacity:.9"></div>
<div class="abs social-text">
  <p>Since the commencement of our activity, R. T. Holloway, Inc. contributes to change the quality of life of children and seniors across the world, providing them with support for primary education and basic medical aid, which we believe to be the right of every human being.</p>
  <p>Proportionally to our growth, R. T. Holloway, Inc. aims to extend our contributions to other communities in Africa and the rest of the World, with more donations to charities and other non-profit organizations via the Rowan T. Holloway Foundation (https://rth-foundation.org/en/)</p>
</div>

<!-- footer -->
<footer class="abs site-footer"></footer>
<div class="abs brand" style="left:485px;top:3325px">
  <div class="brand-mark" style="width:82px;height:82px;margin-bottom:14px"></div>
  <div class="brand-name" style="font-size:38px;line-height:42px">R. T. Holloway</div>
  <div class="brand-inc" style="font-size:22px;line-height:26px">Inc.</div>
</div>
<div class="abs contact-chip" style="left:386px;top:3540px">
  <svg width="46" height="46" viewBox="0 0 46 46"><circle cx="23" cy="23" r="21" fill="none" stroke="#b39b5e" stroke-width="2"/><rect x="17" y="12" width="12" height="22" rx="2" fill="none" stroke="#b39b5e" stroke-width="2"/><line x1="21" y1="30" x2="25" y2="30" stroke="#b39b5e" stroke-width="2"/></svg>
  <div><div class="chip-label">Phone:</div><div class="chip-value">+1000 000-0000</div></div>
</div>
<div class="abs contact-chip" style="left:582px;top:3540px">
  <svg width="46" height="46" viewBox="0 0 46 46"><circle cx="23" cy="23" r="21" fill="none" stroke="#b39b5e" stroke-width="2"/><rect x="13" y="16" width="20" height="14" fill="none" stroke="#b39b5e" stroke-width="2"/><polyline points="13,16 23,24 33,16" fill="none" stroke="#b39b5e" stroke-width="2"/></svg>
  <div><div class="chip-label">Mail:</div><div class="chip-value">info@rtholloway.com</div></div>
</div>
<nav class="abs footer-nav">HOME &nbsp;|&nbsp; ABOUT US &nbsp;|&nbsp; INVESTMENT AREAS &nbsp;|&nbsp; SOCIAL RESPONSIBILITY &nbsp;|&nbsp; CONTACT US</nav>
<div class="abs footer-rule"></div>
<div class="abs copyright">Copyrights @ 2021 RT Holloway. All Rights Reserved.</div>

</body>
</html>
```